Harlow Pennick Group Business Cards

We have a new logo, and want to design new business cards with it. We are 21 years in business, and want a fresh but professional look, so not a lot of extra stuff on the card. We are a recruiting and staffing firm focused on placing accounting and finance professionals in the Dallas TX area. I've attached our new logo that should be displayed on the cards. Here is what I think we want on the cards:
Ned Varcombe, CPA
Partner and Managing Director
8262 Quarry Mill Rd.
Suite 610
Dallas, TX 75391
O 214-583-9071
M 214-690-1482
ned@harlowpennick-example.com
www.harlowpennick-example.com

```html
<!DOCTYPE html>
<html lang="en">
<head>
<meta charset="utf-8">
<title>Harlow Pennick Group – Business Card</title>
<link href="https://fonts.googleapis.com/css2?family=Michroma&family=Arimo:wght@400&display=swap" rel="stylesheet">
<style>
  :root {
    --navy: #1f2a63;
    --navy-soft: #3a4a8c;
    --ink: #3d3f4a;
    --card-top: #f4f6fa;
    --card-bottom: #e3e7ef;
    --page: #d9d6d1;
    --white: #ffffff;
  }
  html, body {
    margin: 0;
    padding: 0;
    width: 1200px;
    height: 970px;
    overflow: hidden;
    background: var(--page);
  }
  .card {
    position: absolute;
    left: 80px;
    top: 190px;
    width: 1040px;
    height: 590px;
    border-radius: 28px;
    background: linear-gradient(160deg, var(--card-top) 0%, #eef1f7 45%, var(--card-bottom) 100%);
    box-shadow: 0 10px 30px rgba(0,0,0,0.18);
    overflow: hidden;
    font-family: "Arimo", Arial, sans-serif;
    color: var(--ink);
  }
  .brand-name {
    position: absolute;
    left: 190px;
    top: 295px;
    transform: translate(-50%, -50%) rotate(-90deg);
    white-space: nowrap;
    font-family: "Michroma", sans-serif;
    font-size: 26px;
    letter-spacing: 1px;
    color: var(--navy);
  }
  .web-band {
    position: absolute;
    right: 0;
    top: 0;
    width: 56px;
    height: 430px;
  }
  .web-address {
    position: absolute;
    left: 1012px;
    top: 185px;
    transform: translate(-50%, -50%) rotate(-90deg);
    white-space: nowrap;
    font-size: 20px;
    color: var(--white);
    letter-spacing: 0.3px;
  }
  .person-name {
    position: absolute;
    left: 325px;
    top: 358px;
    margin: 0;
    font-family: "Michroma", sans-serif;
    font-weight: 400;
    font-size: 27px;
    color: var(--navy);
    letter-spacing: 0.5px;
  }
  .person-title {
    position: absolute;
    left: 325px;
    top: 392px;
    margin: 0;
    font-size: 22px;
    color: var(--ink);
  }
  .divider {
    position: absolute;
    left: 325px;
    top: 435px;
    width: 660px;
    height: 2px;
    background: var(--navy);
  }
  .contact-list {
    position: absolute;
    left: 325px;
    top: 455px;
    margin: 0;
    padding: 0;
    list-style: none;
  }
  .contact-list li {
    display: flex;
    align-items: center;
    height: 33.5px;
    font-size: 23px;
  }
  .contact-list svg {
    width: 26px;
    height: 26px;
    margin-right: 14px;
    flex: none;
  }
  .address {
    position: absolute;
    right: 55px;
    top: 452px;
    margin: 0;
    font-style: normal;
    text-align: right;
    font-size: 23px;
    line-height: 33.5px;
    color: var(--ink);
  }
</style>
</head>
<body>
  <div class="card">
    <div class="brand-name">HARLOW PENNICK GROUP</div>

    <svg class="web-band" viewBox="0 0 56 430" aria-hidden="true">
      <path d="M0 0 H28 A28 28 0 0 1 56 28 V430 L0 350 Z" fill="var(--navy)"/>
    </svg>
    <div class="web-address">www.harlowpennick-example.com</div>

    <h1 class="person-name">NED VARCOMBE, CPA</h1>
    <p class="person-title">Partner and Managing Director</p>
    <div class="divider"></div>

    <ul class="contact-list">
      <li>
        <svg viewBox="0 0 26 26" aria-label="Office phone">
          <circle cx="13" cy="13" r="11.5" fill="none" stroke="var(--navy-soft)" stroke-width="2"/>
          <path d="M7.5 10 Q13 6 18.5 10 L17 12 H9 Z M9 13 H17 L18 18 H8 Z" fill="var(--navy-soft)"/>
        </svg>
        214-583-9071
      </li>
      <li>
        <svg viewBox="0 0 26 26" aria-label="Mobile phone">
          <circle cx="13" cy="13" r="11.5" fill="none" stroke="var(--navy-soft)" stroke-width="2"/>
          <rect x="9" y="7" width="8" height="12" rx="1.5" fill="none" stroke="var(--navy-soft)" stroke-width="1.8"/>
        </svg>
        214-690-1482
      </li>
      <li>
        <svg viewBox="0 0 26 26" aria-label="Email">
          <circle cx="13" cy="13" r="11.5" fill="none" stroke="var(--navy-soft)" stroke-width="2"/>
          <rect x="7" y="9" width="12" height="8.5" fill="var(--navy-soft)"/>
          <path d="M7 9 L13 14 L19 9" fill="none" stroke="var(--white)" stroke-width="1.2"/>
        </svg>
        ned@harlowpennick-example.com
      </li>
    </ul>

    <address class="address">
      8262 Quarry Mill Rd.<br>
      Suite 610<br>
      Dallas, TX 75391
    </address>
  </div>
</body>
</html>
```